Website Design Project

KEL VISA is looking for a professional designer who would re-design our current website www.bordwellpassage.com.
KEL provides immigration and visa services to the US in these markets: Slovakia, Czech republic and USA. We would like to target Poland and Russia as well.
Who are we: KEL is Dubrik & Helmsley international law firm with offices in New York, Bratislava and Prague. We are licensed in several jurisdiction such as New York, England and Wales, and Slovakia.
Additionally, we are offering online products in our E-shop, such as E-books, E-brochures, DVD's regarding visa and immigration opportunities into United States.
Our targeted audience is: young students who want to study in the US, young professionals looking for employment in the US, investors who want to invest to the US, people looking to get their green card (permanent residency in the US), etc.
Our new design: should look professional, communicate financial safety, professional services, increase sales, but also feel emotional for people who are looking forward to start their new life in the United States.
Updates

Dear Designers, 

we have changed our project from refundable to committed! 

Cant wait to see your designs! 

Thanks! 

KEL VISA 

Designers! 

We have attached pictures od old NY so you may wanna work with them! 

Target Market(s)

USA, Slovakia, Czech Republic

Industry/Entity Type

Financial

Requirements
Nice to have
• 1) pictures of old New York, Tarrow Quay.
2) pictures of the US
Should not have
• KEL VISA is operated by law form Dubrik & Helmsley. We are not looking for boring, old fashioned and profesional website for "legal practitioners". No dark colors, no brown color, no dark green color. it should look light and fresh.

KEL VISA is fresh, new, modern, professional and flexible TEAM of YOUNG and SMART immigration lawyers who want to make a difference. Our website MUST reflect our philosophy. "Success is all about people that we meet and the things we create with them".

```html
<!DOCTYPE html>
<html lang="en">
<head>
<meta charset="utf-8">
<title>KEL Visa and Immigration</title>
<link href="https://fonts.googleapis.com/css2?family=Open+Sans:wght@400;600;700&display=swap" rel="stylesheet">
<style>
:root{
  --navy:#0b3a6e;
  --blue:#1565b0;
  --blue-light:#2a86d6;
  --yellow:#f6c21a;
  --yellow-dark:#e2a90c;
  --orange:#f39a1c;
  --text:#444;
  --muted:#777;
  --line:#dde3ea;
  --footer:#0c3566;
  --footer-dark:#082748;
  --page:#ffffff;
}
*{box-sizing:border-box;margin:0;padding:0}
html,body{width:753px;height:1200px;overflow:hidden;background:var(--page)}
body{font-family:"Open Sans",Arial,sans-serif;color:var(--text);font-size:7px;line-height:1.5}
.site{width:753px;height:1200px;position:relative}
.header{height:75px;display:flex;justify-content:space-between;align-items:center;padding:0 14px 0 12px}
.brand{display:flex;align-items:center;gap:8px}
.brand-mark{width:30px;height:30px;border-radius:50%;background:var(--blue)}
.brand-name{font-size:19px;font-weight:700;color:var(--navy);line-height:1}
.brand-tag{font-size:6px;color:var(--muted);margin-top:3px}
.contact{text-align:right}
.contact-mail{font-size:6.5px;color:var(--muted)}
.contact-phone{font-size:17px;font-weight:700;color:var(--navy);display:flex;align-items:center;gap:5px;justify-content:flex-end}
.nav{height:18px;background:linear-gradient(var(--yellow),var(--yellow-dark));display:flex;padding-left:8px}
.nav a{font-size:6.5px;font-weight:600;color:#5a3c00;text-decoration:none;padding:0 10px;line-height:18px;border-right:1px solid rgba(255,255,255,.5)}
.nav a.active{background:#fff;color:var(--navy)}
.hero{height:283px;position:relative;background:
  linear-gradient(180deg,rgba(230,232,235,.9) 0%,rgba(200,204,209,.2) 35%,rgba(70,76,84,.0) 60%),
  linear-gradient(90deg,#9aa0a7 0%,#c4c8cc 30%,#b3b8be 55%,#8d939a 80%,#a7acb2 100%);}
.hero::after{content:"";position:absolute;left:0;right:0;bottom:0;height:110px;background:linear-gradient(180deg,rgba(90,96,104,0),#5c636b)}
.hero-dots{position:absolute;bottom:8px;left:50%;transform:translateX(-50%);display:flex;gap:4px;z-index:1}
.hero-dots span{width:5px;height:5px;border-radius:50%;background:#fff;opacity:.6}
.hero-dots span:first-child{opacity:1}
.content{display:flex;padding:18px 12px 0;gap:22px;height:610px}
.main{width:482px}
.sidebar{width:225px}
h1{font-size:13px;color:var(--navy);font-weight:600;margin-bottom:10px}
h2{font-size:12px;color:var(--navy);font-weight:600;margin:60px 0 12px}
.main p{margin-bottom:10px;color:var(--muted);font-size:7px;line-height:13px}
.products{display:grid;grid-template-columns:repeat(3,1fr);gap:22px 16px;width:430px}
.product{display:flex;gap:7px;align-items:flex-end}
.product-shot{width:66px;height:80px;background:linear-gradient(#eef1f5,#cfd6df);border:1px solid var(--line)}
.product-name{font-size:6.5px;color:var(--muted)}
.product-price{font-size:15px;color:var(--navy);font-weight:600;line-height:1.2}
.buy{display:inline-block;background:var(--orange);color:#fff;font-size:6.5px;font-weight:700;padding:3px 8px;border-radius:2px;margin-top:3px}
.side-title{font-size:12px;color:var(--navy);font-weight:600;margin-bottom:8px}
.side-list{list-style:none;margin-bottom:16px}
.side-list li{font-size:6.5px;color:var(--blue);padding:5px 0 5px 9px;border-bottom:1px solid var(--line);position:relative}
.side-list li::before{content:"";position:absolute;left:1px;top:9px;width:3px;height:3px;background:var(--blue);border-radius:50%}
.offer{height:26px;margin-bottom:3px;background:linear-gradient(var(--blue-light),var(--blue));display:flex;justify-content:space-between;align-items:center;padding:0 10px;color:var(--yellow);font-weight:700;font-size:8px}
.offer .price{font-size:10px}
.offer.dark{background:linear-gradient(#1d76c4,var(--navy))}
.most{margin-top:40px}
.footer{height:185px;background:var(--footer);display:flex;padding:16px 12px 0;gap:12px;color:#a9c2de}
.footer-col{width:138px}
.footer-col h3{font-size:9px;color:#fff;font-weight:600;margin-bottom:7px}
.footer-col li{list-style:none;font-size:6.5px;line-height:1.75}
.social{display:flex;gap:5px;margin-top:7px}
.social span{width:10px;height:10px;background:#a9c2de;border-radius:2px}
.bottom{height:29px;background:var(--footer-dark);color:#7f9bbd;font-size:6px;display:flex;justify-content:space-between;align-items:center;padding:0 12px}
</style>
</head>
<body>
<div class="site">
  <header class="header">
    <div class="brand">
      <div class="brand-mark"></div>
      <div>
        <div class="brand-name">KEL Visa and Immigration</div>
        <div class="brand-tag">Dubrik &amp; Helmsley, Immigration Attorneys, 30 Bay, US Green Card, ESTA</div>
      </div>
    </div>
    <div class="contact">
      <div class="contact-mail">office@bordwellpassage.com</div>
      <div class="contact-phone">
        <svg width="12" height="12" viewBox="0 0 24 24" fill="#0b3a6e"><path d="M6.6 10.8a15 15 0 0 0 6.6 6.6l2.2-2.2a1 1 0 0 1 1-.25 11.4 11.4 0 0 0 3.6.6 1 1 0 0 1 1 1V20a1 1 0 0 1-1 1A17 17 0 0 1 3 4a1 1 0 0 1 1-1h3.5a1 1 0 0 1 1 1c0 1.25.2 2.45.6 3.6a1 1 0 0 1-.25 1z"/></svg>
        212-555-0148
      </div>
    </div>
  </header>
  <nav class="nav">
    <a class="active">Consultation</a><a>Visitors Visas</a><a>Work Visas</a><a>Business Visas</a><a>Family Visas</a><a>Student Visas</a><a>Green Card</a><a>Visa Forms</a><a>KEL E-shop</a><a>Visa News</a>
  </nav>
  <div class="hero" role="img" aria-label="Black and white photograph of the old New York skyline">
    <div class="hero-dots"><span></span><span></span><span></span><span></span></div>
  </div>
  <div class="content">
    <section class="main">
      <h1>Visas to the U.S. and U.S. Immigration</h1>
      <p>KEL Visa and Immigration USA aids travelers in the process of obtaining green cards or different visas to enter the United States. A tourist may obtain a visa to the United States from a counselor of the USA, and must show it upon entry to the country. The immigration lawyer or passport control can authorize the visa holder entry, determine the length of stay, or deny entry to the U.S.</p>
      <p>Our immigration staff is experienced in different visas for the United States. We are here for travelers with tourism, family, student, trade, and other travel documents. Contact us today if you have any issues of which visa you need to visit the United States, and we will manage the process for you. For students we offer forms for visas of types F1, J1, M1. For studying at a high school or college, a F1 visa is needed. The J1 visa is ideal for attending a college or university, while employees and the M1 visa should be used by any students attending a college or university. These visas are all temporary and will need to be renewed each term.</p>
      <p>The E-2 visa is for individuals who are investing in a business for a substantial profit. This visa to the U.S will only be approved for citizens of partnering countries. We are currently preparing lists for more information and guides on investment visas and other assistance. If you are traveling with a loved one, family, or tour group we offer visa advice and answer all questions for each trip to the States.</p>
      <h2>Buy Online Products</h2>
      <div class="products">
        <div class="product"><div class="product-shot" role="img" aria-label="E-book cover"></div><div><div class="product-name">E-book Name</div><div class="product-price">$24.99</div><span class="buy">Buy Now</span></div></div>
        <div class="product"><div class="product-shot" role="img" aria-label="E-brochure cover"></div><div><div class="product-name">E-brochures</div><div class="product-price">$14.99</div><span class="buy">Buy Now</span></div></div>
        <div class="product"><div class="product-shot" role="img" aria-label="DVD case"></div><div><div class="product-name">DVD's</div><div class="product-price">$9.99</div><span class="buy">Buy Now</span></div></div>
        <div class="product"><div class="product-shot" role="img" aria-label="E-book cover"></div><div><div class="product-name">E-book Name</div><div class="product-price">$24.99</div><span class="buy">Buy Now</span></div></div>
        <div class="product"><div class="product-shot" role="img" aria-label="E-brochure cover"></div><div><div class="product-name">E-brochures</div><div class="product-price">$14.99</div><span class="buy">Buy Now</span></div></div>
        <div class="product"><div class="product-shot" role="img" aria-label="DVD case"></div><div><div class="product-name">DVD's</div><div class="product-price">$9.99</div><span class="buy">Buy Now</span></div></div>
      </div>
    </section>
    <aside class="sidebar">
      <div class="side-title">Recent Blog Posts</div>
      <ul class="side-list">
        <li>Applying For Your F1 Passport</li>
        <li>E-1V Immigrant Visa to the US</li>
        <li>Senator Hale and the Immigration Policy</li>
        <li>How to Get a Student Visa to the US</li>
        <li>A Probable Vote on Immigration Reform in the U.S.</li>
      </ul>
      <div class="offer"><span>Visa Forms Download</span><span class="price">Free</span></div>
      <div class="offer dark"><span>Working Visa for 6 Months</span><span class="price">$1000</span></div>
      <div class="offer"><span>Tourist Visa for 6 Months</span><span class="price">$300</span></div>
      <div class="offer dark"><span>ESTA Registration</span><span class="price">$30</span></div>
      <div class="offer"><span>Consultation</span><span class="price">$65</span></div>
      <div class="side-title most">Most Viewed</div>
      <ul class="side-list">
        <li>How to Get to the U.S.</li>
        <li>E-2 Visa and L-1 Visa – How to Become "Legal" Entrepreneur in the U.S.</li>
        <li>How to Become a 1-Way Exchange Visitor Without Paying Unnecessary Fees</li>
        <li>Electronic Diversity Visa Draw – Register Early</li>
        <li>E-2 Visa and L-1 Visa – How to Become "Legal" Entrepreneur in the U.S.</li>
      </ul>
    </aside>
  </div>
  <footer class="footer">
    <div class="footer-col"><h3>Quick Links</h3><ul><li>Home</li><li>Consultation</li><li>Visitors Visas</li><li>Work Visas</li><li>Business Visas</li><li>Family Visas</li></ul></div>
    <div class="footer-col"><h3>About Us</h3><ul><li>About the Company</li><li>What We Do</li><li>Business Blog</li><li>Most Viewed</li><li>Online Products</li><li>Contact Us</li></ul></div>
    <div class="footer-col"><h3>Support</h3><ul><li>America Useful Tools</li><li>Information</li><li>Green Card</li><li>Citizenships</li><li>Contracts</li><li>FAQ</li></ul></div>
    <div class="footer-col"><h3>Links</h3><ul><li>Fenwick Partners, Immigration Lawyers</li><li>Larkmoor Group, Business Advisory</li><li>Partner Pages</li><li>Dubrik &amp; Helmsley - US Consultation</li><li>England Hong Kong or Offshore</li></ul></div>
    <div class="footer-col"><h3>Contact Information</h3><ul><li>Dubrik &amp; Helmsley Legal Services</li><li>Tarrow Quay Office</li><li>118 W 96th Street Ave</li><li>New York, NY 10000</li><li>+1 (212) 555-0148</li></ul><div class="social"><span></span><span></span></div></div>
  </footer>
  <div class="bottom"><span>© 2013 Company Name. All rights reserved.</span><span>Top</span></div>
</div>
</body>
</html>
```